Dravel

We are openıng one huntıng showroom in Riyadh? Saudi Arabia. Company name is "DRAVEL".
Our logo designed and we need Business Card Design now.
I attached DRAVEL logo below.
Front side will English and back side will be Arabic

```html
<!DOCTYPE html>
<html lang="en">
<head>
<meta charset="utf-8">
<title>Dravel — Business Card</title>
<link rel="stylesheet" href="https://fonts.googleapis.com/css2?family=Signika:wght@400;600;700&family=Noto+Kufi+Arabic:wght@400;700&display=swap">
<style>
  :root {
    --green-dark: #0b6b3c;
    --green-light: #6b9a3a;
    --ink: #2b2b2b;
    --paper: #fafafa;
    --backdrop: #e4e4e2;
  }
  * { box-sizing: border-box; margin: 0; padding: 0; }
  html, body { width: 1200px; height: 1021px; overflow: hidden; }
  body {
    background: var(--backdrop);
    font-family: "Signika", sans-serif;
    color: var(--ink);
    position: relative;
  }
  .card {
    position: absolute;
    top: 110px;
    width: 457px;
    height: 800px;
    background: var(--paper);
    box-shadow: 0 6px 18px rgba(0,0,0,0.12);
    overflow: hidden;
  }
  .card--front { left: 110px; }
  .card--back { left: 633px; direction: rtl; font-family: "Noto Kufi Arabic", sans-serif; }

  .edge-band {
    position: absolute;
    top: 0; bottom: 0;
    width: 26px;
    background: linear-gradient(to bottom,
      var(--green-dark) 0 60%,
      var(--green-light) 60% 88%,
      var(--green-dark) 88% 100%);
  }
  .card--front .edge-band { left: 0; }
  .card--back .edge-band { right: 0; }

  .wordmark {
    position: absolute;
    top: 90px;
    left: 0; right: 0;
    text-align: center;
    font-family: "Signika", sans-serif;
    font-weight: 700;
    font-size: 100px;
    line-height: 1;
    color: var(--green-dark);
    direction: ltr;
  }
  .card--front .wordmark { padding-left: 26px; }
  .card--back .wordmark { padding-right: 26px; }

  .details {
    position: absolute;
    top: 400px;
  }
  .card--front .details { left: 66px; }
  .card--back .details { right: 66px; text-align: right; }

  .person-name {
    font-weight: 700;
    font-size: 30px;
    color: var(--green-dark);
    line-height: 1.1;
  }
  .card--back .person-name { font-size: 26px; }
  .person-role {
    font-size: 24px;
    line-height: 1.3;
    margin-bottom: 44px;
  }
  .card--back .person-role { font-size: 20px; }
  .address {
    font-size: 22px;
    line-height: 1.4;
    margin-bottom: 6px;
  }
  .card--back .address { font-size: 19px; }
  .contact-list { list-style: none; }
  .contact-item {
    display: flex;
    align-items: center;
    gap: 8px;
    font-size: 22px;
    line-height: 1.4;
    font-family: "Signika", sans-serif;
  }
  .card--back .contact-item { direction: rtl; }
  .contact-item span { direction: ltr; }
  .contact-icon { width: 18px; height: 18px; flex: none; }
</style>
</head>
<body>

  <section class="card card--front" aria-label="Front of business card">
    <div class="edge-band"></div>
    <div class="wordmark">DRAVEL</div>
    <div class="details">
      <p class="person-name">Layth Haddad</p>
      <p class="person-role">Founder</p>
      <p class="address">Floor 9, Nakheel Tower<br>Olaya Street, Riyadh 12214</p>
      <ul class="contact-list">
        <li class="contact-item">
          <svg class="contact-icon" viewBox="0 0 20 20"><path d="M5 2l3 4-2 2c1 2 3 4 5 5l2-2 4 3-2 3C9 17 3 11 2 4z" fill="var(--green-dark)"/></svg>
          <span>+966 55 204 8817</span>
        </li>
        <li class="contact-item">
          <svg class="contact-icon" viewBox="0 0 20 20"><rect x="1.5" y="4" width="17" height="12" fill="none" stroke="var(--green-dark)" stroke-width="2"/><path d="M2 5l8 6 8-6" fill="none" stroke="var(--green-dark)" stroke-width="2"/></svg>
          <span>layth@dravel.com</span>
        </li>
        <li class="contact-item">
          <svg class="contact-icon" viewBox="0 0 20 20"><circle cx="10" cy="10" r="8.5" fill="var(--green-dark)"/><path d="M2 10h16M10 2c-4 4-4 12 0 16M10 2c4 4 4 12 0 16" fill="none" stroke="#fff" stroke-width="1.2"/></svg>
          <span>www.dravel.com</span>
        </li>
      </ul>
    </div>
  </section>

  <section class="card card--back" lang="ar" aria-label="Back of business card">
    <div class="edge-band"></div>
    <div class="wordmark">DRAVEL</div>
    <div class="details">
      <p class="person-name">ليث حداد</p>
      <p class="person-role">مؤسس</p>
      <p class="address">الطابق ٩، برج النخيل<br>شارع العليا، الرياض 12214</p>
      <ul class="contact-list">
        <li class="contact-item">
          <svg class="contact-icon" viewBox="0 0 20 20"><path d="M5 2l3 4-2 2c1 2 3 4 5 5l2-2 4 3-2 3C9 17 3 11 2 4z" fill="var(--green-dark)"/></svg>
          <span>+966 55 204 8817</span>
        </li>
        <li class="contact-item">
          <svg class="contact-icon" viewBox="0 0 20 20"><rect x="1.5" y="4" width="17" height="12" fill="none" stroke="var(--green-dark)" stroke-width="2"/><path d="M2 5l8 6 8-6" fill="none" stroke="var(--green-dark)" stroke-width="2"/></svg>
          <span>layth@dravel.com</span>
        </li>
        <li class="contact-item">
          <svg class="contact-icon" viewBox="0 0 20 20"><circle cx="10" cy="10" r="8.5" fill="var(--green-dark)"/><path d="M2 10h16M10 2c-4 4-4 12 0 16M10 2c4 4 4 12 0 16" fill="none" stroke="#fff" stroke-width="1.2"/></svg>
          <span>www.dravel.com</span>
        </li>
      </ul>
    </div>
  </section>

</body>
</html>
```